Postcard Design

I need to have a Table Tent made for our Restaurant. On one side is the Burger Specials and the other side is Happy Hour Drink specials. Our colors are black and white in the restaurant. We need a slightly larger font as our customers are older. The cost of the burgers is $13 each. we are an old school steak house.

Restaurant

```html
<!DOCTYPE html>
<html lang="en">
<head>
<meta charset="utf-8">
<title>Burger Specials and Happy Hour Table Tent</title>
<link rel="stylesheet" href="https://fonts.googleapis.com/css2?family=Josefin+Sans:wght@400;600;700&family=Montserrat:wght@700&family=Arimo:wght@400;700&display=swap">
<style>
  :root {
    --orange: #f9a932;
    --gold: #e8b04a;
    --ink: #0d0808;
    --panel: #1f1d1d;
    --white: #ffffff;
    --rule: #555555;
  }
  * { margin: 0; padding: 0; box-sizing: border-box; }
  html, body { width: 884px; height: 1200px; overflow: hidden; }
  body { background: var(--orange); position: relative; font-family: "Josefin Sans", sans-serif; color: var(--white); }

  .front { position: absolute; left: 14px; top: 13px; width: 848px; height: 570px; background: var(--panel); overflow: hidden; }
  .dining-photo { position: absolute; left: 0; top: 0; width: 440px; height: 570px;
    background: linear-gradient(160deg, #5a2a17 0%, #3b1a10 35%, #7a4a2e 60%, #2c1710 100%); }
  .torn-edge { position: absolute; left: 420px; top: 0; width: 40px; height: 570px; }

  .menu-item { position: absolute; }
  .menu-item h2 { font-family: "Montserrat", sans-serif; font-weight: 700; text-transform: uppercase; letter-spacing: 0.3px; display: flex; justify-content: space-between; }
  .menu-item .price { color: var(--orange); }
  .front .menu-item { left: 465px; width: 366px; }
  .front .menu-item h2 { font-size: 18.5px; line-height: 22px; }
  .front .menu-item p { font-size: 15.4px; line-height: 19.8px; letter-spacing: 0.2px; }

  .back { position: absolute; left: 11px; top: 608px; width: 447px; height: 572px; background: var(--ink); }
  .back .menu-item { left: 31px; width: 400px; }
  .back .menu-item h2 { font-size: 17.5px; line-height: 21px; }
  .back .menu-item p { font-size: 13.6px; line-height: 19.5px; font-weight: 600; }
  .hours-note { position: absolute; left: 31px; top: 406px; font-family: "Montserrat", sans-serif; font-weight: 700; font-size: 16px; color: var(--orange); text-transform: uppercase; }

  .mailing { position: absolute; left: 458px; top: 608px; width: 404px; height: 572px; background: var(--white); color: #111; font-family: "Arimo", sans-serif; }
  .return-address { position: absolute; left: 29px; top: 34px; font-size: 10.2px; line-height: 14.5px; font-style: normal; }
  .return-address strong { font-size: 11px; }
  .postage { position: absolute; left: 328px; top: 22px; width: 58px; height: 58px; border: 1px solid #333; font-size: 9.5px; display: flex; align-items: center; justify-content: center; }
  .address-line { position: absolute; left: 29px; width: 357px; border-top: 2px solid var(--rule); }
</style>
</head>
<body>
  <section class="front">
    <div class="dining-photo" role="img" aria-label="Guests dining at a white-clothed table in a warm wood-panelled steakhouse room"></div>
    <svg class="torn-edge" viewBox="0 0 40 570" preserveAspectRatio="none" aria-hidden="true">
      <path d="M20 0 L26 20 L18 45 L27 70 L19 95 L28 120 L20 150 L27 175 L18 205 L26 235 L19 260 L28 290 L20 320 L27 345 L18 375 L26 405 L19 430 L28 460 L20 490 L27 515 L19 545 L25 570 L40 570 L40 0 Z" fill="#1f1d1d"/>
      <path d="M20 0 L26 20 L18 45 L27 70 L19 95 L28 120 L20 150 L27 175 L18 205 L26 235 L19 260 L28 290 L20 320 L27 345 L18 375 L26 405 L19 430 L28 460 L20 490 L27 515 L19 545 L25 570" fill="none" stroke="#e8b04a" stroke-width="6"/>
    </svg>

    <div class="menu-item" style="top:30px">
      <h2>BBQ Bacon Burger <span class="price">$13</span></h2>
      <p>(bacon, cheddar, onion rings, bbq sauce, lettuce, tomato), your choice of side.</p>
    </div>
    <div class="menu-item" style="top:111px">
      <h2>Green Chile Burger <span class="price">$13</span></h2>
      <p>(mustard, pickles, tomato,onions. american cheese, hatch green chile), your choice of side</p>
    </div>
    <div class="menu-item" style="top:194px">
      <h2>Grilled Cheicken BLT <span class="price">$13</span></h2>
      <p>(grilled chicken, mozzarella, bacon, lettuce, tomato, mayo), your choice of side</p>
    </div>
    <div class="menu-item" style="top:277px">
      <h2>Shrimp Brochette <span class="price">$13</span></h2>
      <p>(pepper jack cheese, jalapeno, bacon, served over dirty rice)</p>
    </div>
    <div class="menu-item" style="top:359px">
      <h2>No Carb Burger <span class="price">$13</span></h2>
      <p>Lettuce sheets as your bun, meat patty, cheese if you like, lettuce, tomato, onions, mayo, mustard and your choice of side</p>
    </div>
    <div class="menu-item" style="top:459px">
      <h2>Spicy Lettuce Wraps</h2>
      <p>Lettuce&nbsp; shredded, pico de gallo, cabbage, choose (Chicken, shrimp or steak), queso-fresco, sriracha sauce and your choice of side</p>
    </div>
  </section>

  <section class="back">
    <div class="menu-item" style="top:28px">
      <h2>House Old Fashioned <span class="price">$7</span></h2>
      <p>bourbon, bitters, sugar, orange peel and a cherry, served over a large ice cube</p>
    </div>
    <div class="menu-item" style="top:98px">
      <h2>Classic Martini <span class="price">$7</span></h2>
      <p>gin or vodka, dry vermouth, stirred cold, with olives or a lemon twist</p>
    </div>
    <div class="menu-item" style="top:168px">
      <h2>Manhattan <span class="price">$7</span></h2>
      <p>rye whiskey, sweet vermouth, bitters, served up with a cherry</p>
    </div>
    <div class="menu-item" style="top:238px">
      <h2>House Wines <span class="price">$6</span></h2>
      <p>red or white by the glass, ask your server for tonight's pours</p>
    </div>
    <div class="menu-item" style="top:308px">
      <h2>Draft Beers <span class="price">$4</span></h2>
      <p>all local and domestic drafts, served in a frosted pint glass</p>
    </div>
    <p class="hours-note">Happy Hour Daily 4 to 6 PM</p>
  </section>

  <section class="mailing">
    <address class="return-address">
      <strong>Restaurant</strong><br>
      1800 Larchmont Building<br>
      215 Carver Street<br>
      Milltown, PA 15000
    </address>
    <div class="postage">POSTAGE</div>
    <div class="address-line" style="top:198px"></div>
    <div class="address-line" style="top:244px"></div>
    <div class="address-line" style="top:287px"></div>
    <div class="address-line" style="top:333px"></div>
  </section>
</body>
</html>
```